Wine Label Design for Marrick Estate

I need a front and back label for a new wine I am making. I am looking for a classic, elegant and serious wine label. I would like the label to be white with blue and black writing. The blue will be the distinction in the label. The color of blue will be unique and catch the eye. The font of the writing will be unique and could also serve as the brand image for Marrick Estate. The label can have a design but should be simple and distinct. I envision the paper quality of the label to textured, high quality and add to the overall image of the label.
The label will be timeless. The price of this wine will be $85.00 a bottle, and the label should match a higher priced wine. This wine is family owned and operated.
The writing on the front and back label will be:

FRONT Label-

Marrick Estate

Howell Mountain

Napa Valley

2022 Cabernet Sauvignon

Back Label-

Cellared and Bottled by Marrick Estate, Calder Ridge, CA 94000

GOVERNMENT WARNING: (1) According to the Surgeon General, women should not drink alcoholic beverages during pregnancy because of the risk of birth defects. (2) Consumption of alcoholic beverages impairs your ability to drive a car or operate machinery, and may cause health problems.

Alc. 14.5% by Vol.

750 ml

Contains Sulfites

```html
<!DOCTYPE html>
<html lang="en">
<head>
<meta charset="utf-8">
<title>Marrick Estate – Wine Labels</title>
<link href="https://fonts.googleapis.com/css2?family=Lora:wght@400;600&family=Montserrat:wght@400&family=Quattrocento:wght@400&display=swap" rel="stylesheet">
<style>
  :root {
    --estate-blue: #12509b;
    --ink: #161616;
    --paper: #f6f6f4;
    --paper-shade: #ecece9;
    --backdrop: #000000;
  }
  * { margin: 0; padding: 0; box-sizing: border-box; }
  html, body { width: 1200px; height: 796px; overflow: hidden; background: var(--backdrop); }
  .stage { position: relative; width: 1200px; height: 796px; }

  .label {
    position: absolute;
    top: 170px;
    width: 395px;
    height: 522px;
    background: radial-gradient(ellipse at 40% 30%, var(--paper) 0%, var(--paper-shade) 100%);
  }
  .label--front { left: 187px; }
  .label--back { left: 617px; }

  /* Front label */
  .front-ornament {
    position: absolute; left: 152px; top: 27px; width: 91px; height: 22px;
    background: linear-gradient(90deg, transparent, rgba(18,80,155,0.35), transparent);
    border-radius: 11px;
  }
  .front-brand {
    position: absolute; left: 0; right: 0; top: 84px;
    text-align: center;
    font-family: "Lora", serif; font-weight: 400;
    font-size: 44px; line-height: 50px; letter-spacing: 1px;
    color: var(--estate-blue); text-transform: uppercase;
  }
  .front-subregion {
    position: absolute; left: 0; right: 0; top: 238px;
    text-align: center;
    font-family: "Montserrat", sans-serif; font-size: 26px; letter-spacing: 0.5px;
    color: var(--ink);
  }
  .front-region-lettering {
    position: absolute; left: 103px; top: 326px; width: 195px; height: 38px;
    background: linear-gradient(90deg, rgba(18,80,155,0.12), rgba(18,80,155,0.28), rgba(18,80,155,0.12));
    border-radius: 4px;
  }
  .front-vintage {
    position: absolute; left: 0; right: 0; top: 410px;
    text-align: center;
    font-family: "Quattrocento", serif; font-size: 30px; color: var(--estate-blue);
  }
  .front-varietal {
    position: absolute; left: 0; right: 0; top: 444px;
    text-align: center;
    font-family: "Quattrocento", serif; font-size: 35px; color: var(--ink);
  }

  /* Back label */
  .back-band {
    height: 101px; background: var(--estate-blue);
    display: flex; align-items: center; justify-content: center;
    text-align: center;
    font-family: "Lora", serif; font-size: 19px; line-height: 23px; color: #ffffff;
  }
  .back-warning {
    padding: 24px 14px 0 14px;
    font-family: "Lora", serif; font-size: 20.5px; line-height: 26.6px;
    color: var(--ink); text-align: justify; hyphens: manual;
  }
  .back-warning__title {
    display: block; font-weight: 600; font-size: 17.5px; line-height: 24px;
    color: var(--estate-blue);
  }
  .back-alcohol {
    position: absolute; left: 0; right: 0; top: 388px;
    text-align: center;
    font-family: "Lora", serif; font-weight: 600; font-size: 21px; color: var(--estate-blue);
  }
  .back-volume {
    position: absolute; left: 162px; top: 437px; width: 72px; height: 25px;
    background: var(--estate-blue); color: #ffffff;
    font-family: "Lora", serif; font-size: 18px; line-height: 25px; text-align: center;
  }
  .back-sulfites {
    position: absolute; left: 0; right: 0; top: 485px;
    text-align: center;
    font-family: "Lora", serif; font-size: 18px; letter-spacing: 2.5px; color: var(--ink);
  }
</style>
</head>
<body>
<main class="stage">
  <section class="label label--front" aria-label="Front label">
    <div class="front-ornament" role="img" aria-label="Blue decorative flourish"></div>
    <h1 class="front-brand">Marrick<br>Estate</h1>
    <p class="front-subregion">Howell Mountain</p>
    <div class="front-region-lettering" role="img" aria-label="Napa Valley in blue hand lettering"></div>
    <p class="front-vintage">2022</p>
    <p class="front-varietal">Cabernet Sauvignon</p>
  </section>

  <section class="label label--back" aria-label="Back label">
    <header class="back-band">Cellared and Bottled by Marrick Estate,<br>Calder Ridge, CA 94000</header>
    <p class="back-warning">
      <span class="back-warning__title">GOVERNMENT WARNING:</span>
      (1)&nbsp; According to the Surgeon General, women should not drink alcoholic beverages during pregnancy because of the risk of birth defects.<br>
      (2)&nbsp; Consumption of alcoholic bever&shy;ages impairs your ability to drive a car or operate machinery, and may cause health problems.
    </p>
    <p class="back-alcohol">Alc. 14.5% by Vol.</p>
    <p class="back-volume">750 ml</p>
    <p class="back-sulfites">Contains Sulfites</p>
  </section>
</main>
</body>
</html>
```